Sleek business card design for digital agency.

Brief document attached for detailed description and inspiration. Looking for a minimalist sleek, cool, modern business card design.

Industry/Entity Type

Digital

```html
<!DOCTYPE html>
<html lang="en">
<head>
<meta charset="utf-8">
<title>Flint Works — Business Card</title>
<link rel="stylesheet" href="https://fonts.googleapis.com/css2?family=Great+Vibes&family=Questrial&display=swap">
<style>
  :root {
    --backdrop-light: #f4f4f4;
    --backdrop-dark: #9a9a9a;
    --card-black: #050505;
    --card-white: #ffffff;
    --ink: #111111;
    --ink-soft: #2a2a2a;
    --mark-silver: #d9d9d9;
    --accent-blue: #2b3fa8;
    --social-blue: #3a4fb8;
  }
  * { margin: 0; padding: 0; box-sizing: border-box; }
  html, body { width: 1200px; height: 900px; overflow: hidden; }
  body {
    background: radial-gradient(ellipse at 50% 45%, var(--backdrop-light) 0%, #e2e2e2 45%, var(--backdrop-dark) 100%);
    font-family: "Questrial", "Century Gothic", sans-serif;
    position: relative;
  }
  .card {
    position: absolute;
    width: 500px;
    height: 286px;
    box-shadow: 0 6px 18px rgba(0,0,0,0.25);
  }
  /* Front */
  .card-front {
    left: 170px; top: 150px;
    background: var(--card-black);
    display: flex; align-items: center; justify-content: center; gap: 16px;
  }
  .brand-dot {
    width: 38px; height: 38px; border-radius: 50%;
    background: var(--mark-silver);
  }
  .brand-name {
    color: var(--mark-silver);
    font-size: 44px;
    letter-spacing: 1px;
  }
  /* Back */
  .card-back {
    left: 530px; top: 460px;
    background: var(--card-white);
    overflow: hidden;
    color: var(--ink);
  }
  .details { position: absolute; left: 24px; top: 16px; }
  .person-name {
    font-family: "Great Vibes", cursive;
    font-size: 44px; font-weight: 400; line-height: 1;
    margin-bottom: 2px;
  }
  .role, .drink { font-size: 13px; line-height: 1.25; color: var(--ink-soft); }
  .contact {
    margin-top: 12px;
    display: grid; grid-template-columns: 48px auto;
    font-size: 11px; line-height: 1.3; column-gap: 6px;
  }
  .address {
    margin-top: 10px;
    font-size: 11px; line-height: 1.3; text-transform: uppercase;
    padding-bottom: 6px;
    border-bottom: 2px solid var(--accent-blue);
    width: 178px;
  }
  .social {
    margin-top: 6px;
    display: grid; grid-template-columns: 62px auto;
    font-size: 11px; line-height: 1.3; color: var(--social-blue);
  }
  .corner-emblem {
    position: absolute; right: 0; bottom: 0;
  }
</style>
</head>
<body>
  <section class="card card-front" aria-label="Card front">
    <span class="brand-dot"></span>
    <span class="brand-name">Flint Works</span>
  </section>

  <section class="card card-back" aria-label="Card back">
    <div class="details">
      <h1 class="person-name">Daniel Hart</h1>
      <p class="role">Marketing Director</p>
      <p class="drink">Drink order: G&amp;T with cucumber</p>
      <div class="contact">
        <span>Mobil:</span><span>0400 128 476</span>
        <span>Phone:</span><span>03 9000 4821</span>
        <span>Email:</span><span>dhart@flintworks.com</span>
      </div>
      <p class="address">Level 2, 18 Quarry St<br>East Harbour NSW 2000</p>
      <div class="social">
        <span>Facebook:</span><span>/FlintWorks</span>
        <span>Website:</span><span>www.FlintWorks.com</span>
      </div>
    </div>
    <svg class="corner-emblem" width="230" height="286" viewBox="0 0 230 286" role="img" aria-label="Large black brand emblem silhouette filling the corner">
      <path d="M230 0 L230 286 L20 286 Q40 200 120 170 Q150 90 230 0 Z" fill="var(--card-black)"/>
    </svg>
  </section>
</body>
</html>
```